School Signage

I am wanting designs for signs completed that prompt students of the school requirements for hats, preparation and play.

I've uploaded rough examples of what we're after, but we would like them stylised and better than the example, including:
- A stylised logo/graphic for the 'Mervale 1, 2, 3'
- Clear, crisp signage for the words.
- Graphics that reinforce the message of the sign.

We're after three signs:
- One that will be located on the oval to prompt hat use.
- One that will be near the entry prompting the morning routine (please make this one landscape with instructions for 'on time' on one side, and 'late' on the other).
- One that will be located within the school prompting readiness for class.

```html
<!DOCTYPE html>
<html lang="en">
<head>
<meta charset="utf-8">
<title>Mervale 1.2.3 School Signage</title>
<link rel="stylesheet" href="https://fonts.googleapis.com/css2?family=Lilita+One&family=Nunito+Sans:ital,wght@1,700;1,800&family=Montserrat:wght@600;800&family=Allura&display=swap">
<style>
:root{
  --bg:#4a4a4a;
  --paper:#ffffff;
  --ink:#111111;
  --green:#3f9a4a;
  --green-soft:#7cc46e;
  --green-deep:#2f7d40;
  --yellow:#f4d23a;
  --yellow-soft:#f8e27a;
}
*{box-sizing:border-box;margin:0;padding:0}
html,body{width:1200px;height:600px;overflow:hidden;background:var(--bg)}
.sign{position:absolute;background:var(--paper);overflow:hidden}
.sign--routine{left:20px;top:120px;width:520px;height:360px}
.sign--ready{left:560px;top:83px;width:300px;height:435px}
.sign--hats{left:880px;top:83px;width:300px;height:435px}

.wash{position:absolute;border-radius:46% 54% 58% 42%/50% 44% 56% 50%}
.wash--y{background:radial-gradient(circle at 45% 45%,var(--yellow) 0%,var(--yellow-soft) 60%,rgba(248,226,122,.3) 100%)}
.wash--g{background:radial-gradient(circle at 45% 45%,var(--green) 0%,var(--green-soft) 65%,rgba(124,196,110,.35) 100%);opacity:.85}
.wash--lg{background:radial-gradient(circle at 50% 50%,var(--green-soft) 0%,rgba(124,196,110,.5) 70%,rgba(124,196,110,.15) 100%)}
.dot{position:absolute;border-radius:50%;background:var(--green-soft)}
.ring{position:absolute;border-radius:50%;border:2px solid var(--green)}

.title{position:absolute;font-family:"Lilita One",sans-serif;font-weight:400;color:var(--ink);text-align:center;transform:rotate(-4deg);line-height:1}
.title .lead{display:block;font-size:19px}
.title .lead .big{font-size:26px}
.title .name{display:block;font-size:34px;letter-spacing:.5px}
.title .num{display:block;font-size:40px;letter-spacing:-2px}

.steps{position:absolute;font-family:"Nunito Sans",sans-serif;font-style:italic;font-weight:700;color:var(--ink);width:215px}
.steps h3{font-size:12.5px;font-weight:800;text-decoration:underline;margin-bottom:8px}
.step{display:flex;align-items:center;gap:7px;font-size:10.5px;line-height:1.3;margin-bottom:9px}
.step svg{flex:none}
.steps--late h3{text-align:right}
.steps--late .step{justify-content:flex-end;text-align:right}
.divider{position:absolute;left:259px;top:138px;width:1px;height:118px;background:var(--green)}
.slogan{position:absolute;left:262px;top:262px;font-family:"Allura",cursive;font-size:26px;line-height:.95;transform:rotate(-8deg);color:var(--ink)}
.slogan span{display:block}
.slogan span+span{padding-left:30px}

.items{position:absolute;left:42px;top:168px;font-family:"Nunito Sans",sans-serif;font-style:italic;font-weight:800;font-size:16.5px;color:var(--ink)}
.item{display:flex;align-items:center;gap:10px;height:52px}
.item svg{flex:none}

.actions{position:absolute;left:104px;top:208px;font-family:"Nunito Sans",sans-serif;font-style:italic;font-weight:800;font-size:18px;color:var(--ink)}
.action{display:flex;align-items:center;gap:8px;height:54px}
.action svg{flex:none}

.footer{position:absolute;left:22px;bottom:18px;display:flex;align-items:center;gap:8px}
.brand{display:flex;flex-direction:column;align-items:center;gap:2px;width:40px}
.brand-mark{width:22px;height:22px;border-radius:50%;background:var(--green-deep)}
.brand-name{font-family:"Montserrat",sans-serif;font-weight:800;font-size:7px;color:var(--green-deep);letter-spacing:.3px}
.motto{font-family:"Montserrat",sans-serif;font-weight:800;font-size:15px;color:var(--ink);line-height:1}
.motto small{display:block;font-weight:600;font-size:10px}
</style>
</head>
<body>

<section class="sign sign--routine">
  <div class="wash wash--y" style="left:400px;top:-40px;width:150px;height:150px"></div>
  <div class="wash wash--g" style="left:470px;top:110px;width:90px;height:160px"></div>
  <div class="wash wash--g" style="left:-50px;top:60px;width:100px;height:150px"></div>
  <div class="wash wash--y" style="left:-40px;top:210px;width:100px;height:120px"></div>
  <div class="dot" style="left:64px;top:40px;width:11px;height:11px"></div>
  <div class="dot" style="left:14px;top:240px;width:26px;height:26px;background:var(--green)"></div>

  <h1 class="title" style="left:130px;top:16px;width:260px">
    <span class="lead">Morning Routine:</span>
    <span class="name">The Mervale</span>
    <span class="num">1.2.3</span>
  </h1>

  <div class="steps steps--ontime" style="left:32px;top:134px">
    <h3>ON TIME:</h3>
    <div class="step"><svg width="18" height="18" viewBox="0 0 20 20"><circle cx="10" cy="10" r="9" fill="#7cb342"/><circle cx="10" cy="10" r="6.5" fill="#fff"/><path d="M10 6v4l3 2" stroke="#333" stroke-width="1.4" fill="none"/></svg>Arrive before 8:30 AM</div>
    <div class="step"><svg width="18" height="18" viewBox="0 0 20 20"><rect x="1" y="2" width="8" height="16" rx="1" fill="#6b8fc7"/><rect x="11" y="2" width="8" height="16" rx="1" fill="#6b8fc7"/></svg>Drop bag at locker and<br>collect learning materials</div>
    <div class="step"><svg width="18" height="18" viewBox="0 0 20 20"><rect x="3" y="4" width="14" height="15" rx="4" fill="#e8a23a"/><rect x="6" y="11" width="8" height="5" rx="1" fill="#c9822a"/></svg>Arrive at Home Group /<br>House Assembly before 8:40 AM</div>
  </div>

  <div class="divider"></div>

  <div class="steps steps--late" style="right:32px;top:134px">
    <h3>RUNNING LATE:</h3>
    <div class="step">Arrive before 8:30 AM<svg width="18" height="18" viewBox="0 0 18 18"><rect x="2" y="7" width="14" height="10" fill="#d9823b"/><path d="M1 8 9 2l8 6z" fill="#b8562b"/></svg></div>
    <div class="step">Drop bag at locker and<br>collect learning materials<svg width="18" height="18" viewBox="0 0 18 20"><rect x="1" y="1" width="7" height="18" rx="1" fill="#6b8fc7"/><rect x="10" y="1" width="7" height="18" rx="1" fill="#6b8fc7"/></svg></div>
    <div class="step">Arrive at Home Group /<br>House Assembly before 8:40 AM<svg width="18" height="18" viewBox="0 0 20 18"><rect x="3" y="7" width="14" height="10" fill="#4a7fb5"/><path d="M1 8 10 1l9 7z" fill="#d9823b"/></svg></div>
  </div>

  <p class="slogan"><span>Early is on time,</span><span>on time is late!</span></p>

  <div class="footer">
    <div class="brand"><span class="brand-mark"></span><span class="brand-name">MERVALE</span></div>
    <p class="motto"><small>EXCEED YOUR</small>EXPECTATION</p>
  </div>
</section>

<section class="sign sign--ready">
  <div class="wash wash--lg" style="left:-20px;top:-35px;width:165px;height:112px"></div>
  <div class="wash wash--g" style="left:248px;top:78px;width:78px;height:95px"></div>
  <div class="wash wash--y" style="left:232px;top:146px;width:86px;height:172px"></div>
  <div class="wash wash--g" style="left:-34px;top:190px;width:68px;height:130px"></div>
  <div class="wash wash--y" style="left:146px;top:343px;width:163px;height:112px"></div>
  <div class="wash wash--lg" style="left:188px;top:352px;width:128px;height:112px"></div>
  <div class="dot" style="left:255px;top:155px;width:20px;height:20px;background:var(--green)"></div>
  <div class="dot" style="left:258px;top:296px;width:8px;height:8px"></div>

  <h1 class="title" style="left:15px;top:38px;width:260px">
    <span class="lead">Are you ready for class?</span>
    <span class="name">The Mervale</span>
    <span class="num">1.2.3</span>
  </h1>

  <div class="items">
    <div class="item"><svg width="30" height="26" viewBox="0 0 32 28"><rect x="4" y="2" width="24" height="17" rx="2" fill="#2d5a87"/><rect x="6" y="4" width="20" height="13" fill="#6fb3e0"/><path d="M0 21h32l-3 5H3z" fill="#2d5a87"/></svg>Laptop/workbook</div>
    <div class="item"><svg width="30" height="32" viewBox="0 0 32 34"><rect x="9" y="3" width="14" height="29" rx="4" fill="#1f8a7a"/><rect x="12" y="7" width="8" height="6" rx="1" fill="#0f5c52"/></svg>Phone in Lockpouch</div>
    <div class="item"><svg width="30" height="24" viewBox="0 0 36 26"><path d="M4 18a14 14 0 0 1 28 0z" fill="#e8b92e"/><path d="M4 18h30l-4 4H6z" fill="#c99a1f"/></svg><span>Correct uniform<br>(including hat)</span></div>
  </div>

  <div class="footer">
    <div class="brand"><span class="brand-mark"></span><span class="brand-name">MERVALE</span></div>
    <p class="motto">CURIOSITY AND DRIVE</p>
  </div>
</section>

<section class="sign sign--hats">
  <div class="wash wash--y" style="left:218px;top:-17px;width:103px;height:155px"></div>
  <div class="wash wash--y" style="left:240px;top:128px;width:86px;height:137px"></div>
  <div class="wash wash--g" style="left:-34px;top:128px;width:78px;height:112px"></div>
  <div class="wash wash--lg" style="left:-17px;top:163px;width:95px;height:112px"></div>
  <div class="wash wash--g" style="left:172px;top:318px;width:155px;height:137px"></div>
  <div class="wash wash--g" style="left:70px;top:392px;width:70px;height:52px"></div>
  <div class="ring" style="left:253px;top:232px;width:70px;height:128px"></div>

  <h1 class="title" style="left:25px;top:22px;width:250px">
    <span class="lead">We wear <span class="big">HATS</span></span>
    <span class="lead" style="font-size:22px">at Mervale</span>
    <span class="lead">When <span style="font-size:22px">OUTDOORS..</span></span>
    <span class="name">The Mervale</span>
    <span class="num">1.2.3</span>
  </h1>

  <div class="actions">
    <div class="action"><svg role="img" aria-label="Walking pictogram" width="22" height="30" viewBox="0 0 22 30" fill="none" stroke="#2f7d40" stroke-width="3" stroke-linecap="round"><circle cx="12" cy="4" r="3" fill="#2f7d40" stroke="none"/><path d="M11 9l-2 9M10 11l-5 5M11 11l5 4M9 18l-4 10M9 18l5 4 1 6"/></svg>Walking</div>
    <div class="action"><svg role="img" aria-label="Sitting pictogram" width="22" height="30" viewBox="0 0 22 30" fill="none" stroke="#2f7d40" stroke-width="3" stroke-linecap="round"><circle cx="8" cy="4" r="3" fill="#2f7d40" stroke="none"/><path d="M8 9v10h8v9M8 12l6 3M3 14v14M3 21h15"/></svg>Sitting</div>
    <div class="action"><svg role="img" aria-label="Playing ball pictogram" width="24" height="30" viewBox="0 0 24 30" fill="none" stroke="#2f7d40" stroke-width="3" stroke-linecap="round"><circle cx="9" cy="4" r="3" fill="#2f7d40" stroke="none"/><path d="M9 9l-1 9M8 11l-5 3M9 11l5 3M8 18l-4 10M8 18l7 5"/><circle cx="20" cy="26" r="3" fill="#2f7d40" stroke="none"/></svg>Playing</div>
  </div>

  <div class="footer">
    <div class="brand"><span class="brand-mark"></span><span class="brand-name">MERVALE</span></div>
    <p class="motto">INTEGRITY</p>
  </div>
</section>

</body>
</html>
```